2017 Summer Camp Marketing Poster

We need a poster 11 X 17 to advertise our summer 2017 programs for Camp Tellumar and direct interested people to our website tellumar.org.

The poster will grab peoples eye especially kids and make them want to further explore our camp.

There will be a call to action "Sign up today for the summer of a lifetime"

The poster will primarily be hung in churches where most people know about the camp but need reminded of our summer camp programs and dates.

Target Market(s)

Kids and Families

Industry/Entity Type

Marketing

Font styles to use
Sans Serif

```html
<!DOCTYPE html>
<html lang="en">
<head>
<meta charset="utf-8">
<title>Camp Tellumar 2017 Summer Camp Poster</title>
<link rel="stylesheet" href="https://fonts.googleapis.com/css2?family=Baloo+2:wght@600;700;800&family=Fredoka:wght@600;700&display=swap">
<style>
  :root {
    --stage: #2b2b2b;
    --navy: #2e2b6e;
    --sun: #fcd20a;
    --lime: #b9c22a;
    --grass: #3d8f2e;
    --grass-light: #5cae3f;
    --red: #e23b26;
    --orange: #f28a16;
    --green: #2f9a3a;
    --ink: #2a1e4f;
    --white: #ffffff;
  }
  * { box-sizing: border-box; margin: 0; padding: 0; }
  html, body { width: 1200px; height: 1200px; overflow: hidden; background: var(--stage); }
  .poster {
    position: absolute; left: 231px; top: 30px;
    width: 738px; height: 1140px; overflow: hidden;
    background: var(--navy);
    font-family: "Baloo 2", sans-serif;
  }
  .hero-photo {
    position: absolute; left: 0; top: 0; width: 738px; height: 560px;
    background: linear-gradient(160deg, #1f3320 0%, #3b4d35 35%, #7b8fa8 55%, #4b5a3c 80%, #2a3a24 100%);
  }
  .brand {
    position: absolute; left: 52px; top: 48px;
    display: flex; align-items: center; gap: 10px;
    font-family: "Baloo 2", sans-serif; font-weight: 800; font-size: 40px;
    color: var(--white); line-height: 1;
  }
  .brand-dot { width: 18px; height: 18px; border-radius: 50%; background: var(--white); }
  .grass {
    position: absolute; left: 0; top: 545px; width: 738px; height: 330px;
    background: radial-gradient(circle at 30% 40%, var(--grass-light), var(--grass) 70%);
  }
  .title-banner {
    position: absolute; left: 10px; top: 442px; width: 690px; height: 204px;
    background: var(--sun);
    border-radius: 70px 90px 80px 60px / 60px 80px 70px 60px;
    transform: rotate(-1deg);
  }
  .title-year {
    position: absolute; left: 0; right: 30px; top: 452px; text-align: center;
    font-family: "Fredoka", sans-serif; font-weight: 700; font-size: 50px; line-height: 1;
    color: var(--red); -webkit-text-stroke: 2px var(--white); paint-order: stroke fill;
    text-shadow: 0 3px 0 rgba(0,0,0,.15);
  }
  .title-main {
    position: absolute; left: 0; right: 20px; top: 505px; text-align: center;
    font-family: "Fredoka", sans-serif; font-weight: 700; font-size: 82px; line-height: 1;
    letter-spacing: -2px; -webkit-text-stroke: 2px var(--white); paint-order: stroke fill;
    text-shadow: 0 3px 0 rgba(0,0,0,.15);
  }
  .c-red { color: var(--red); } .c-orange { color: var(--orange); } .c-green { color: var(--green); }
  .tagline {
    position: absolute; left: 0; right: 40px; top: 597px; text-align: center;
    font-family: "Fredoka", sans-serif; font-weight: 600; font-size: 21px;
    color: var(--ink); transform: rotate(-1deg);
  }
  .snapshot {
    position: absolute; border: 6px solid var(--white);
    box-shadow: 0 3px 8px rgba(0,0,0,.35);
  }
  .snapshot-group { left: 59px; top: 665px; width: 236px; height: 195px; transform: rotate(-1deg);
    background: linear-gradient(180deg, #8fa27a 0%, #6e5a46 40%, #c56fa5 60%, #4f8a3a 100%); }
  .snapshot-ropes { left: 306px; top: 672px; width: 182px; height: 158px; transform: rotate(1.5deg);
    background: linear-gradient(180deg, #2f4a2a, #5b7d48 55%, #3a5530); }
  .snapshot-chapel { left: 500px; top: 648px; width: 185px; height: 165px; transform: rotate(5deg);
    background: linear-gradient(180deg, #dfe6ef 0%, #a33a33 40%, #6f8f4b 70%, #9a9a8a 100%); }
  .stripe-band { position: absolute; left: 0; top: 820px; width: 738px; height: 70px; }
  .signup {
    position: absolute; left: 0; right: 0; top: 890px; text-align: center; color: var(--white);
  }
  .signup-head { font-weight: 800; font-size: 56px; line-height: 1; }
  .signup-sub { font-weight: 700; font-size: 27px; line-height: 1.2; margin-top: 2px; }
  .footer-curve { position: absolute; left: 0; top: 1015px; width: 738px; height: 125px; }
  .web-address {
    position: absolute; left: 0; right: 0; top: 1052px; text-align: center;
    font-weight: 800; font-size: 54px; line-height: 1; color: var(--white);
    text-shadow: 0 3px 4px rgba(0,0,0,.45);
  }
</style>
</head>
<body>
  <main class="poster">
    <div class="hero-photo" role="img" aria-label="Photo of smiling campers in climbing helmets holding ropes in the woods"></div>
    <div class="brand"><span class="brand-dot"></span>Tellumar</div>

    <div class="grass" role="img" aria-label="Green grass texture"></div>

    <div class="title-banner"></div>
    <div class="title-year">2017 TELLUMAR</div>
    <div class="title-main">
      <span class="c-red">S</span><span class="c-green">U</span><span class="c-orange">M</span><span class="c-green">M</span><span class="c-orange">E</span><span class="c-green">R</span>
      <span class="c-orange">C</span><span class="c-red">A</span><span class="c-green">M</span><span class="c-orange">P</span>
    </div>
    <div class="tagline">Fun &amp; Creative Outdoor Activities!</div>

    <div class="snapshot snapshot-group" role="img" aria-label="Photo of the whole camp group in front of the lodge"></div>
    <div class="snapshot snapshot-ropes" role="img" aria-label="Photo of a camper crossing a rope bridge course"></div>
    <div class="snapshot snapshot-chapel" role="img" aria-label="Photo of campers walking by the red chapel and cross"></div>

    <svg class="stripe-band" viewBox="0 0 738 70" preserveAspectRatio="none" aria-hidden="true">
      <defs>
        <pattern id="candy" width="40" height="20" patternUnits="userSpaceOnUse" patternTransform="skewX(-45)">
          <rect width="40" height="20" fill="#3a9a34"/>
          <rect width="20" height="20" fill="#ffffff"/>
        </pattern>
      </defs>
      <polygon points="0,52 738,22 738,40 0,70" fill="url(#candy)"/>
      <polygon points="0,70 738,40 738,70" fill="#2e2b6e"/>
    </svg>

    <div class="signup">
      <div class="signup-head">Sign Up Today</div>
      <div class="signup-sub">for the summer of a lifetime</div>
    </div>

    <svg class="footer-curve" viewBox="0 0 738 125" preserveAspectRatio="none" aria-hidden="true">
      <path d="M0,66 Q369,-10 738,66 L738,125 L0,125 Z" fill="#b9c22a"/>
    </svg>
    <div class="web-address">www.tellumar.org</div>
  </main>
</body>
</html>
```